HIgh-end jewelry designer needs a business card design

I need a business card design for the ecclectic & rather expensive jewelry designs. My approach to my work is to combine very old jewelry offset with contemporary items. I enjoy the idea of legacy as well as repurposing finely crafted items that are not possible to create any longer. My desire is to celebrate the past in a contemporary & funky way. The name of my business is MERIVALE. I see my business card design as simple & yet enigmatic as possible. In the end... clean, simple & understated is the look I am after. Thank you for your consideration...

Target Market(s)

I will use this business card for the trade as well as customers

Industry/Entity Type

Business

Contact Information for Business Card

Corinne Halvard Owner/Designer 555-274-8163

Requirements
Must have
• Clean & simple sophisticated design using the word "Merivalle" as the logo. I like the idea of a play on the word itself, perhaps even using different fonts (i.e.: a bold helvetica combined with a lovely script). I'm afraid to say more because I don't want to limit creative input. Gosh, sometimes it's ok to break the rules!
Nice to have
• In my mind, I have imagined this business card to be simple, using my company name "Merivale" in a playful yet sophisticated manner. I believe that doing something beautifully simple can be a true challenge. I have imagined something with just black & white, however I am open to ideas... after all that's why I'm here!
Should not have
• As Mozart once said... "It has too many notes!" I know I'm being silly, but I don't want it to be complicated or overly ornate.

```html
<!DOCTYPE html>
<html lang="en">
<head>
<meta charset="utf-8">
<title>Merivalle — Business Card</title>
<link href="https://fonts.googleapis.com/css2?family=Bodoni+Moda:opsz,wght@6..96,400&display=swap" rel="stylesheet">
<style>
  :root {
    --paper: #ffffff;
    --ink: #0a0a0a;
    --logo-tone: #8c8c8c;
    --sketch-light: #e6e6e6;
    --sketch-dark: #3a3a3a;
    --serif: "Bodoni Moda", "Didot", "Times New Roman", serif;
  }
  html, body {
    margin: 0;
    padding: 0;
    overflow: hidden;
    background: var(--paper);
  }
  .card {
    position: relative;
    width: 1200px;
    height: 702px;
    overflow: hidden;
    font-family: var(--serif);
    background: var(--paper);
  }
  .card__dark-half {
    position: absolute;
    top: 0;
    left: 600px;
    width: 600px;
    height: 702px;
    background: var(--ink);
  }
  .floral-bouquet {
    position: absolute;
    left: 0;
    top: 250px;
    width: 600px;
    height: 452px;
    background: linear-gradient(180deg, rgba(230,230,230,0) 0%, var(--sketch-light) 55%, #cfcfcf 100%);
  }
  .floral-bloom {
    position: absolute;
    left: 1034px;
    top: 498px;
    width: 166px;
    height: 204px;
    background: radial-gradient(circle at 60% 40%, var(--sketch-dark) 0%, #1c1c1c 60%, var(--ink) 100%);
  }
  .wordmark {
    position: absolute;
    left: 196px;
    top: 40px;
    margin: 0;
    font-weight: 400;
    font-size: 186px;
    line-height: 1;
    letter-spacing: -2px;
    color: var(--logo-tone);
  }
  .tagline {
    position: absolute;
    right: 166px;
    top: 216px;
    margin: 0;
    font-size: 19px;
    color: var(--paper);
    letter-spacing: 0.2px;
  }
  .contact-block {
    position: absolute;
    left: 600px;
    width: 470px;
    text-align: center;
    color: var(--paper);
  }
  .person {
    top: 300px;
  }
  .person__name {
    margin: 0;
    font-size: 54px;
    font-weight: 400;
    line-height: 1.1;
  }
  .person__role {
    margin: 2px 0 0;
    font-size: 30px;
    line-height: 1.2;
  }
  .reach {
    top: 510px;
  }
  .reach__line {
    margin: 0;
    font-size: 33px;
    line-height: 1.6;
  }
</style>
</head>
<body>
  <main class="card">
    <div class="card__dark-half"></div>

    <div class="floral-bouquet" role="img" aria-label="Pen-and-ink sketch of tulips and a rose growing up from the bottom edge"></div>
    <div class="floral-bloom" role="img" aria-label="Inverted white-line sketch of an open daisy-like bloom in the corner"></div>

    <h1 class="wordmark">Merivalle</h1>
    <p class="tagline">classic-contemporary jewelry</p>

    <section class="contact-block person">
      <h2 class="person__name">Corinne Halvard</h2>
      <p class="person__role">owner/designer</p>
    </section>

    <section class="contact-block reach">
      <p class="reach__line">P: 555.274.8163</p>
      <p class="reach__line">chalvard@merivalle-mail.com</p>
    </section>
  </main>
</body>
</html>
```